依頼詳細
http://www.hanokure.example/のトップページのリニューアルを考えており
そちらのご提案をいただきたいという業務内容です。
コンテンツはそのままで、デザインのみ作成していただきたいというものです。
コーティングなどはございません。
サイズなども特に指定はありません。
イラストレーターにて納品をお願いいたします。
ページ数
1ページ
希望イメージ
シンプル 複雑
単色 カラフル
暗い 明るい
日常 高級
遊び心 厳粛
未来的 伝統的
女性的 男性的
希望する色
青系
納品ファイル
• イラストレーター形式 (.ai)
補足説明
よろしくお願いいたします。
■ 選んだ理由

社内で選定し、一番イメージに近いものを採用させて頂きました。

■ 提案者全員のお礼・コメント

今回弊社のコンペにたくさんの応募をしていただき真に感謝しております。
どの作品も素晴らしいものばかりで、最後まで選定に時間が掛かりました。
また機会がございましたら是非みなさまのお力をお借りさせて下さい。
ありがとうございました。

```html
<!DOCTYPE html>
<html lang="ja">
<head>
<meta charset="utf-8">
<title>羽ノ暮コンクリート工業株式会社</title>
<link href="https://fonts.googleapis.com/css2?family=Noto+Sans+JP:wght@400;500;700&display=swap" rel="stylesheet">
<style>
:root{
  --blue:#1f6fb8;
  --blue-dark:#124a82;
  --blue-light:#dcebf7;
  --orange:#e8841a;
  --ink:#333;
  --muted:#888;
  --line:#d6dde4;
  --bg:#fff;
}
*{box-sizing:border-box;margin:0;padding:0}
html,body{width:771px;height:1200px;overflow:hidden;background:var(--bg)}
body{font-family:"Noto Sans JP",sans-serif;color:var(--ink);font-size:8px;line-height:1.5}
.page{position:relative;width:771px;height:1200px}

/* header */
.site-header{height:44px;display:flex;align-items:center;justify-content:space-between;padding:0 28px 0 40px;border-top:3px solid var(--blue)}
.brand{display:flex;align-items:center;gap:6px;font-size:14px;font-weight:700;color:var(--blue-dark)}
.brand-mark{width:14px;height:14px;background:var(--orange)}
.header-contact{display:flex;align-items:center;gap:6px}
.header-note{font-size:6px;color:var(--muted);text-align:right;margin-right:4px}
.tel-box{display:flex;align-items:center;gap:4px;border:1px solid var(--line);padding:3px 8px;font-size:13px;font-weight:700;color:var(--blue)}
.mail-btn{background:var(--blue);color:#fff;font-size:7px;padding:6px 8px}

/* nav */
.global-nav{height:34px;display:flex;align-items:stretch;padding:0 40px 0 56px;gap:2px;border-bottom:1px solid var(--line)}
.global-nav a{width:66px;display:flex;flex-direction:column;align-items:center;justify-content:center;font-size:7px;color:var(--ink);text-decoration:none;border-left:1px solid var(--line)}
.global-nav a:last-child{border-right:1px solid var(--line)}
.global-nav .dot{width:8px;height:8px;border-radius:50%;background:var(--blue);margin-bottom:3px}

/* hero */
.hero{position:relative;height:178px;background:linear-gradient(180deg,#cdd9e3 0%,#a9b8c4 55%,#7d8a94 100%)}
.hero-copy{position:absolute;right:60px;top:40px;text-align:center}
.hero-copy .sub{font-size:10px;color:var(--orange);font-weight:700}
.hero-copy .title{font-size:30px;font-weight:700;color:var(--blue-dark);border-bottom:2px solid var(--blue);line-height:1.2}
.hero-copy .desc{font-size:6px;color:#333;margin-top:4px}
.arrow{position:absolute;top:50%;transform:translateY(-50%);width:18px;height:18px;border-radius:50%;background:rgba(255,255,255,.8);display:flex;align-items:center;justify-content:center}
.arrow.left{left:12px}.arrow.right{right:12px}

/* product strip */
.product-strip{height:44px;background:var(--blue-light);display:flex;gap:6px;justify-content:center;align-items:center}
.product-strip .item{width:100px;height:30px;background:linear-gradient(135deg,#9fb2c2,#6d8092);position:relative}
.product-strip .item span{position:absolute;left:0;right:0;bottom:0;background:var(--blue);color:#fff;font-size:6px;text-align:center}

/* section heading */
.section-title{font-size:12px;font-weight:700;text-align:center;color:var(--ink)}
.section-title::after{content:"";display:block;width:30px;height:2px;background:var(--blue);margin:5px auto 0}

/* about */
.about{height:140px;padding-top:20px;text-align:center}
.about .lead{color:var(--blue);font-size:10px;margin-top:12px;line-height:1.7}
.about .body{font-size:6px;color:var(--muted);margin-top:8px;line-height:1.8}

/* scenes */
.scenes{position:relative;height:220px;background:linear-gradient(180deg,#6d94b8,#3f6f9c);padding-top:14px}
.scenes .bar{width:200px;margin:0 auto;background:#fff;padding:4px 0;text-align:center;font-size:10px;font-weight:700;color:var(--blue-dark)}
.scenes .note{text-align:center;color:#fff;font-size:6px;margin-top:8px}
.scene-cards{display:flex;gap:10px;justify-content:center;margin-top:12px}
.scene-card{width:135px;background:#fff}
.scene-card .photo{height:80px;background:linear-gradient(135deg,#b8c6cf,#7f95a3)}
.scene-card p{font-size:7px;text-align:center;padding:4px 0;color:var(--blue-dark);font-weight:500}
.scene-card p small{display:block;font-size:5px;color:var(--muted)}

/* customer */
.customer{height:130px;padding-top:22px;text-align:center}
.customer .body{font-size:6px;color:var(--muted);margin-top:14px;line-height:1.9}

/* banners */
.banners{display:flex;gap:6px;justify-content:center;height:90px}
.banner{width:228px;height:84px;display:flex;flex-direction:column;align-items:center;justify-content:center;gap:6px}
.banner h3{font-size:17px;font-weight:700}
.banner .btn{font-size:6px;padding:2px 12px;border:1px solid currentColor}
.banner.new{background:linear-gradient(135deg,#3a2a1d,#8a5a2e);color:var(--orange)}
.banner.info{background:linear-gradient(135deg,#2b6aa8,#184b7c);color:#fff}
.banner.glossary{background:#eef3f7;color:var(--blue-dark);border:1px solid var(--line)}

/* contact */
.contact{height:150px;display:flex;align-items:center;justify-content:center;gap:40px}
.contact .lead{font-size:11px;font-weight:700;color:var(--blue-dark);margin-bottom:8px}
.contact .tel-btn{display:flex;align-items:center;gap:6px;background:var(--blue);color:#fff;font-size:12px;font-weight:700;padding:5px 14px;width:170px;margin-bottom:5px}
.contact .mail-link{display:block;background:var(--blue-light);color:var(--blue-dark);font-size:8px;padding:5px 14px;width:170px}
.brochure{width:260px;height:110px;background:linear-gradient(135deg,#e9eef2,#b7c5d1)}

/* footer */
.site-footer{border-top:3px solid var(--blue-dark);height:142px;display:flex;padding:16px 40px 0;gap:40px;background:#f6f8fa}
.footer-info .brand{font-size:12px;margin-bottom:6px}
.footer-info p{font-size:6px;color:var(--muted)}
.news h4{font-size:10px;color:var(--blue-dark);border-bottom:1px solid var(--line);padding-bottom:3px;margin-bottom:4px}
.news li{list-style:none;font-size:6px;color:var(--ink);padding:1px 0}
.news li time{color:var(--blue);margin-right:6px}
.copyright{position:absolute;left:0;right:0;bottom:0;height:22px;background:var(--blue-dark);color:#fff;font-size:6px;display:flex;align-items:center;justify-content:flex-end;padding-right:40px}
</style>
</head>
<body>
<div class="page">
  <header class="site-header">
    <div class="brand"><span class="brand-mark"></span>羽ノ暮コンクリート工業株式会社</div>
    <div class="header-contact">
      <div class="header-note">コンクリート二次製品の製造・販売<br>お気軽にお問い合わせください</div>
      <div class="tel-box">
        <svg width="12" height="12" viewBox="0 0 24 24"><path fill="#1f6fb8" d="M6.6 10.8a15 15 0 0 0 6.6 6.6l2.2-2.2a1 1 0 0 1 1-.25 11.4 11.4 0 0 0 3.6.57 1 1 0 0 1 1 1V20a1 1 0 0 1-1 1A17 17 0 0 1 3 4a1 1 0 0 1 1-1h3.5a1 1 0 0 1 1 1c0 1.25.2 2.45.57 3.57a1 1 0 0 1-.25 1z"/></svg>
        078-000-1234
      </div>
      <div class="mail-btn">お問い合わせ</div>
    </div>
  </header>

  <nav class="global-nav">
    <a href="#"><span class="dot"></span>製品案内</a>
    <a href="#"><span class="dot"></span>施工事例</a>
    <a href="#"><span class="dot"></span>新商品</a>
    <a href="#"><span class="dot"></span>会社概要</a>
    <a href="#"><span class="dot"></span>品質管理</a>
    <a href="#"><span class="dot"></span>採用情報</a>
  </nav>

  <section class="hero" role="img" aria-label="コンクリート製品が敷設された道路の写真">
    <div class="arrow left"><svg width="8" height="8" viewBox="0 0 10 10"><path d="M7 1 3 5l4 4" stroke="#1f6fb8" stroke-width="2" fill="none"/></svg></div>
    <div class="hero-copy">
      <div class="sub">道路用コンクリート二次製品</div>
      <div class="title">ロードパネル</div>
      <div class="desc">耐久性と施工性に優れた道路用パネルをご提案します</div>
    </div>
    <div class="arrow right"><svg width="8" height="8" viewBox="0 0 10 10"><path d="M3 1l4 4-4 4" stroke="#1f6fb8" stroke-width="2" fill="none"/></svg></div>
  </section>

  <div class="product-strip">
    <div class="item" role="img" aria-label="製品写真"><span>側溝</span></div>
    <div class="item" role="img" aria-label="製品写真"><span>ボックスカルバート</span></div>
    <div class="item" role="img" aria-label="製品写真"><span>擁壁</span></div>
    <div class="item" role="img" aria-label="製品写真"><span>ロードパネル</span></div>
    <div class="item" role="img" aria-label="製品写真"><span>マンホール</span></div>
    <div class="item" role="img" aria-label="製品写真"><span>その他製品</span></div>
  </div>

  <section class="about">
    <h2 class="section-title">羽ノ暮コンクリート工業について</h2>
    <p class="lead">コンクリートと共に創業50年。<br>これからも各種コンクリート製品の研究開発を通して地域に貢献できる会社を目指します。</p>
    <p class="body">私たちは道路・河川・農業用水路などの社会基盤を支える製品を製造しています。<br>品質と安全を第一に、お客様の信頼に応えるものづくりを続けてまいります。</p>
  </section>

  <section class="scenes">
    <div class="bar">こんなシーンで活躍しています</div>
    <p class="note">当社の製品は道路や河川、水路、宅地造成など様々な現場で使われています。</p>
    <div class="scene-cards">
      <div class="scene-card"><div class="photo" role="img" aria-label="道路の施工現場の写真"></div><p>道路関係<small>側溝・ロードパネル</small></p></div>
      <div class="scene-card"><div class="photo" role="img" aria-label="河川護岸の写真"></div><p>河川関係<small>擁壁・護岸ブロック</small></p></div>
      <div class="scene-card"><div class="photo" role="img" aria-label="宅地造成地の写真"></div><p>宅地造成<small>擁壁・排水製品</small></p></div>
      <div class="scene-card"><div class="photo" role="img" aria-label="農業用水路の写真"></div><p>農業用水路<small>水路・桝</small></p></div>
    </div>
  </section>

  <section class="customer">
    <h2 class="section-title">お客様へ</h2>
    <p class="body">日頃より当社製品をご愛顧いただき誠にありがとうございます。<br>製品の仕様や納期、施工方法などご不明な点がございましたら<br>お気軽に担当者までお問い合わせください。<br>今後とも変わらぬお引き立てを賜りますようお願い申し上げます。</p>
  </section>

  <div class="banners">
    <div class="banner new" role="img" aria-label="新商品の写真を背景にしたバナー"><h3>新商品発売</h3><span class="btn">詳しくはこちら</span></div>
    <div class="banner info"><h3>羽ノ暮情報</h3><span class="btn">詳しくはこちら</span></div>
    <div class="banner glossary"><h3>コンクリート用語集</h3><span class="btn">詳しくはこちら</span></div>
  </div>

  <section class="contact">
    <div>
      <p class="lead">お問い合わせ・資料請求はコチラ</p>
      <div class="tel-btn">
        <svg width="12" height="12" viewBox="0 0 24 24"><path fill="#fff" d="M6.6 10.8a15 15 0 0 0 6.6 6.6l2.2-2.2a1 1 0 0 1 1-.25 11.4 11.4 0 0 0 3.6.57 1 1 0 0 1 1 1V20a1 1 0 0 1-1 1A17 17 0 0 1 3 4a1 1 0 0 1 1-1h3.5a1 1 0 0 1 1 1c0 1.25.2 2.45.57 3.57a1 1 0 0 1-.25 1z"/></svg>
        078-000-1234
      </div>
      <span class="mail-link">メールでのお問い合わせ・資料請求</span>
    </div>
    <div class="brochure" role="img" aria-label="製品カタログの写真"></div>
  </section>

  <footer class="site-footer">
    <div class="footer-info">
      <div class="brand"><span class="brand-mark"></span>羽ノ暮コンクリート工業株式会社</div>
      <p>〒000-0000 兵庫県架空市中央町1-2-3</p>
      <p>TEL 078-000-1234 / FAX 078-000-1235</p>
      <p>http://www.hanokure.example/</p>
    </div>
    <div class="news">
      <h4>新着情報</h4>
      <ul>
        <li><time>2014.10.01</time>新商品ロードパネルを発売しました</li>
        <li><time>2014.09.15</time>ホームページをリニューアルしました</li>
        <li><time>2014.08.20</time>夏季休業のお知らせ</li>
        <li><time>2014.07.10</time>施工事例を追加しました</li>
      </ul>
    </div>
  </footer>
  <div class="copyright">Copyright © Hanokure Concrete Co., Ltd. All Rights Reserved.</div>
</div>
</body>
</html>
```